Global investment holding company - Business Card Design

Kestrel Vane is a recently incorporated investment holding company. Based in Singapore, it has operations in global emerging markets in the transport & logistics, energy and livestock industries.

Its tagline "Alliance for Advancement" reflects the company's philosophy of helping countries progress through partnerships which generate employment and share benefits with its society.

We are looking for a business card that reflects our global presence - incorporating the logo design into the business card design. It must have a sophisticated, modern & corporate feel.

Target Market(s)

Investors and high level governmental officials

Industry/Entity Type

Investment

Requirements
Must have
• - Use of shades of blue in logo

-Profile picture

- Name: Dorian Pike
- Title: Chairman
- Email: dorian@kestrelvane-example.com
- Mob: +65 9104 5821
- Tel: +65 6418 2093
- DID: + 65 6418 2094
- Address: 74 Marlow Road, #08-03, Singapore 048312

- website: www.kestrelvane-example.com

```html
<!DOCTYPE html>
<html lang="en">
<head>
<meta charset="utf-8">
<title>Kestrel Vane – Business Card</title>
<link rel="stylesheet" href="https://fonts.googleapis.com/css2?family=Open+Sans:wght@400;600;700&display=swap">
<style>
  :root {
    --backdrop: #b9b9b9;
    --card-white: #f4f4f4;
    --navy: #1d3c84;
    --navy-deep: #152f6e;
    --brand-blue: #1e3f8c;
    --circle-blue: #3f78c0;
    --ink: #444444;
    --ink-soft: #666666;
    --rule: #8a8a8a;
    --photo-tone: #9ea3a8;
    --white: #ffffff;
  }
  * { box-sizing: border-box; margin: 0; padding: 0; }
  html, body { width: 1200px; height: 720px; overflow: hidden; }
  body {
    background: var(--backdrop);
    font-family: "Open Sans", Arial, sans-serif;
    position: relative;
  }
  .card {
    position: absolute;
    top: 198px;
    width: 540px;
    height: 324px;
    border-radius: 16px;
    overflow: hidden;
  }
  .card--front { left: 40px; background: var(--card-white); color: var(--ink); }
  .card--back {
    left: 620px;
    background: linear-gradient(160deg, var(--navy) 0%, var(--navy-deep) 100%);
    color: var(--white);
  }

  /* Front */
  .brand { position: absolute; left: 30px; top: 22px; display: flex; align-items: center; gap: 12px; }
  .brand__mark { width: 58px; height: 58px; border-radius: 50%; background: var(--circle-blue); flex: none; }
  .brand__name { font-size: 26px; font-weight: 700; line-height: 1; color: var(--brand-blue); letter-spacing: 0.5px; }
  .tagline { position: absolute; left: 30px; top: 92px; font-size: 11.5px; letter-spacing: 1.6px; color: var(--ink-soft); white-space: nowrap; }

  .photo {
    position: absolute; left: 30px; top: 120px;
    width: 130px; height: 130px;
    border: 1px solid #cfcfcf; padding: 5px; background: var(--white);
  }
  .photo__fill { width: 100%; height: 100%; background: linear-gradient(180deg, #b7bcc0, var(--photo-tone)); }

  .person { position: absolute; left: 180px; top: 148px; width: 340px; }
  .person__head { display: flex; align-items: baseline; font-size: 18px; padding-bottom: 6px; border-bottom: 1px solid var(--rule); white-space: nowrap; }
  .person__name { color: var(--brand-blue); }
  .person__sep { margin: 0 22px 0 40px; color: var(--ink-soft); font-size: 14px; }
  .person__title { color: var(--ink); }
  .person__address { font-size: 11px; padding: 6px 0 5px; border-bottom: 1px solid var(--rule); white-space: nowrap; }
  .contacts { display: grid; grid-template-columns: 140px 1fr; gap: 0 8px; font-size: 10.5px; line-height: 1.7; padding-top: 6px; white-space: nowrap; }
  .contacts__email { color: var(--brand-blue); }

  /* Back */
  .back__brand { position: absolute; left: 0; right: 0; top: 82px; display: flex; justify-content: center; align-items: center; gap: 14px; }
  .back__mark { width: 64px; height: 64px; border-radius: 50%; background: var(--white); flex: none; }
  .back__name { font-size: 30px; font-weight: 700; line-height: 1; }
  .back__tagline { position: absolute; left: 0; right: 0; top: 180px; text-align: center; font-size: 12px; letter-spacing: 2px; white-space: nowrap; }
  .back__web { position: absolute; left: 0; right: 0; top: 226px; text-align: center; font-size: 14px; white-space: nowrap; }
</style>
</head>
<body>
  <section class="card card--front" aria-label="Business card front">
    <div class="brand">
      <span class="brand__mark"></span>
      <span class="brand__name">KESTREL<br>VANE</span>
    </div>
    <p class="tagline">ALLIANCE FOR ADVANCEMENT</p>

    <div class="photo">
      <div class="photo__fill" role="img" aria-label="Portrait photo of Dorian Pike"></div>
    </div>

    <div class="person">
      <div class="person__head">
        <span class="person__name">Dorian Pike</span>
        <span class="person__sep">/</span>
        <span class="person__title">Chairman</span>
      </div>
      <p class="person__address">74 Marlow Road, #08-03, Singapore 048312</p>
      <div class="contacts">
        <span>Mob: +65 9104 5821</span>
        <span>DID: + 65 6418 2094</span>
        <span>Tel: +65 6418 2093</span>
        <span class="contacts__email">dorian@kestrelvane-example.com</span>
      </div>
    </div>
  </section>

  <section class="card card--back" aria-label="Business card back">
    <div class="back__brand">
      <span class="back__mark"></span>
      <span class="back__name">KESTREL<br>VANE</span>
    </div>
    <p class="back__tagline">ALLIANCE FOR ADVANCEMENT</p>
    <p class="back__web">www.kestrelvane-example.com</p>
  </section>
</body>
</html>
```